Web Design Project for Harbor Quill

Design a new web site for Harbor Quill.

Current design - www.harborquill-demo.net
Latest design - store.harborquill-demo.net

Close site we like - www.tvx-sample.net

The new design has to be welcoming, fresh, non-industrial, light, friendly and functional.

Target Market(s)

Enterprise IT professionals. In particular, CIO's and IT Managers.

Industry/Entity Type

Store

Requirements
Must have
• Same functionality as the new design.
Should not have
• We want to be able to target different users with different content..... it somethings important to CIO's and not important to Service Delivery Managers, which is different from Network Managers, and different from CFO's.

```html
<!DOCTYPE html>
<html lang="en">
<head>
<meta charset="utf-8">
<title>Harbor Quill — Home</title>
<link href="https://fonts.googleapis.com/css2?family=Arimo:wght@400;700&family=Open+Sans:wght@400;600&display=swap" rel="stylesheet">
<style>
:root{
  --green-deep:#0b5a1e;
  --green-mid:#1a7a2c;
  --green-bright:#2f9a3c;
  --green-accent:#21963a;
  --navy:#13357a;
  --card-blue:#2a6aa8;
  --ink:#333;
  --ink-soft:#555;
  --rule:#c8d0c8;
  --page-top:#ffffff;
  --page-bottom:#e2f1e5;
  --card-bg:#f1f1f4;
}
*{margin:0;padding:0;box-sizing:border-box}
html,body{width:1024px;height:1200px;overflow:hidden}
body{position:relative;font-family:"Arimo",Arial,sans-serif;color:var(--ink);background:linear-gradient(var(--page-top) 500px,var(--page-bottom) 1120px)}
.header{position:absolute;left:0;top:0;width:1024px;height:480px;background:radial-gradient(ellipse at 50% 45%,var(--green-bright) 0%,var(--green-mid) 45%,var(--green-deep) 100%);overflow:hidden}
.header-band{position:absolute;left:0;top:480px;width:1024px;height:8px;background:var(--navy);border-top:2px solid var(--green-deep)}
.brand{position:absolute;left:130px;top:56px;display:flex;align-items:center;gap:8px}
.brand-dot{width:34px;height:34px;border-radius:50%;background:#9fd8a8}
.brand-name{font-size:26px;font-weight:400;color:#cfeed4;letter-spacing:.5px}
.login{position:absolute;right:131px;top:27px;font-size:11.5px;font-weight:700;color:#d6e8d8;text-decoration:underline}
.nav{position:absolute;right:131px;top:56px;display:flex;gap:0;align-items:center;list-style:none}
.nav li{font-size:12.5px;color:#fff;padding:0 5px;line-height:36px}
.nav li.active{background:linear-gradient(#3cae4d,#1f8a30);border:1px solid #55c266;border-radius:2px;padding:0 14px;margin-right:3px;box-shadow:0 2px 4px rgba(0,0,0,.3)}
.hero-photo{position:absolute;left:126px;top:120px;width:777px;height:360px;background:radial-gradient(ellipse at 58% 55%,#c9d8c6 0%,#7a9a7e 35%,rgba(40,110,50,0) 70%)}
.slider-dots{position:absolute;left:492px;top:460px;display:flex;gap:12px}
.slider-dots span{width:13px;height:13px;border-radius:50%;background:#9fbfa2}
.slider-dots span.on{background:#3aa34a}
.content{position:absolute;left:151px;top:500px;width:720px}
.intro-title{font-family:"Open Sans",sans-serif;font-size:19px;color:var(--green-accent);padding-bottom:4px;border-bottom:2px solid var(--rule)}
.intro-title small{font-size:14px;color:#333}
.intro-text{margin-top:8px;font-size:10.5px;line-height:18.5px;text-transform:uppercase;color:var(--ink);word-spacing:1px}
.ticks{list-style:none;margin-top:12px}
.ticks li{display:flex;align-items:center;gap:14px;font-size:10.5px;text-transform:uppercase;height:28px}
.section-title{font-family:"Open Sans",sans-serif;font-size:19px;color:var(--green-accent)}
.section-title span{color:#444}
.solutions{position:absolute;left:151px;top:664px;width:470px}
.solutions .section-title{padding-bottom:4px;border-bottom:1px solid var(--rule)}
.solution-list{list-style:none;margin-top:7px}
.solution-list li{display:flex;align-items:center;gap:10px;font-size:10.5px;color:#333;height:18.4px;padding-left:5px}
.bullet{width:11px;height:11px;border-radius:50%;background:var(--green-accent);position:relative}
.bullet::after{content:"";position:absolute;left:4px;top:3px;border-left:4px solid #fff;border-top:2.5px solid transparent;border-bottom:2.5px solid transparent}
.device-photo{position:absolute;left:497px;top:733px;width:110px;height:113px;border-radius:8px;background:linear-gradient(135deg,#7d8a86,#2d3a36 60%,#4f8a52)}
.news{position:absolute;left:653px;top:664px;width:218px}
.news-list{margin-top:8px;border-left:1px solid var(--rule);margin-left:-12px;padding-left:12px}
.news-item{font-size:10.5px;line-height:18.3px;color:#444;letter-spacing:.3px;margin-bottom:17px}
.read-more{display:block;text-align:center;font-weight:700;color:#777;margin-top:2px}
.read-more u{color:#777}
.cards{position:absolute;left:151px;top:908px;width:720px;display:grid;grid-template-columns:352px 352px;gap:9px 16px}
.card{position:relative;height:92px;background:var(--card-bg);border-top:3px solid #cfd3cf;box-shadow:0 1px 2px rgba(0,0,0,.15)}
.card-art{position:absolute;left:0;top:0;width:104px;height:89px;background:linear-gradient(90deg,#e9f5eb,#5cb26b);border-radius:0 50% 50% 0/0 50% 50% 0}
.card-screen{position:absolute;left:16px;top:26px;width:52px;height:36px;background:linear-gradient(#2f74c0,#174a8a);border:2px solid #c9ced6;border-radius:2px}
.card-body{position:absolute;left:110px;top:4px;width:236px}
.card-title{font-size:12px;color:#444}
.card-title b{color:var(--card-blue)}
.card-text{margin-top:5px;font-size:9.6px;line-height:11px;text-align:justify;color:#333}
.card-more{position:absolute;right:8px;bottom:4px;font-size:9.6px;color:#333}
.footer{position:absolute;left:0;top:1120px;width:1024px;height:80px;background:var(--green-deep);border-top:6px solid var(--navy)}
.copyright{position:absolute;left:150px;top:32px;font-size:10.5px;color:#fff;display:flex;align-items:center;gap:6px}
.copyright b{font-weight:400;color:#b9d9ff}
.footer-nav{position:absolute;right:137px;top:32px;display:flex;gap:11px;list-style:none;font-size:10.5px;color:#fff}
.footer-nav li:first-child{text-decoration:underline}
</style>
</head>
<body>
<header class="header">
  <div class="brand"><span class="brand-dot"></span><span class="brand-name">Harbor Quill</span></div>
  <a class="login">Login/ Register</a>
  <ul class="nav">
    <li class="active">home</li><li>solutions</li><li>technology</li><li>resources</li><li>partners</li><li>company</li><li>support</li>
  </ul>
  <div class="hero-photo" role="img" aria-label="Smiling business professional in front of a team of colleagues"></div>
  <div class="slider-dots"><span></span><span class="on"></span><span></span></div>
</header>
<div class="header-band"></div>

<main class="content">
  <h1 class="intro-title">Industry Leading <small>- helping organisations discover the power of events</small></h1>
  <p class="intro-text">Harbor Quill is proud to announce that it is the gold sponsor of the Northgate CIO Forum 2010 Wednesday, April 7, 2010. Harbor Quill is proud to announce that it is the gold sponsor of the Northgate CIO Forum 2010 Wednesday, April 7, 2010. Announce that it is the gold sponsor of the Northgate CIO Forum 2010 Wednesday, April 7, 2010.</p>
  <ul class="ticks">
    <li><svg width="16" height="14" viewBox="0 0 16 14"><path d="M1 8l4 4L15 1" fill="none" stroke="#21963a" stroke-width="3"/></svg>Announce that it is the gold sponsor of the Northgate CIO Forum 2010 Wednesday, April 7, 2010.</li>
    <li><svg width="16" height="14" viewBox="0 0 16 14"><path d="M1 8l4 4L15 1" fill="none" stroke="#21963a" stroke-width="3"/></svg>Announce that it is the gold sponsor of the Northgate CIO Forum 2010 Wednesday, April 7, 2010.</li>
  </ul>
</main>

<section class="solutions">
  <h2 class="section-title">Harbor Quill <span>Solutions</span></h2>
  <ul class="solution-list">
    <li><span class="bullet"></span>Large Scale Vehicle Tracking with ANPR</li>
    <li><span class="bullet"></span>Real Time Asset Condition Monitoring</li>
    <li><span class="bullet"></span>Customer Experience Monitoring</li>
    <li><span class="bullet"></span>Environmental Monitoring</li>
    <li><span class="bullet"></span>Event Driven Application Platform</li>
    <li><span class="bullet"></span>Information and Communications Technology Monitoring</li>
    <li><span class="bullet"></span>PC Power Management for Workstation Fleets</li>
    <li><span class="bullet"></span>Product Lifecycle Management</li>
    <li><span class="bullet"></span>Security and Surveillance</li>
    <li><span class="bullet"></span>Traffic and Transport Systems</li>
    <li><span class="bullet"></span>Utility Network Management</li>
  </ul>
</section>
<div class="device-photo" role="img" aria-label="Tablet computer showing a green home screen"></div>

<aside class="news">
  <h2 class="section-title">Latest <span>News</span></h2>
  <div class="news-list">
    <div class="news-item">Harbor Quill is proud to announce that it is the Gold Sponsor of the Northgate CIO Forum 2010<br>Wednesday, April 7, 2010<span class="read-more"><u>Read More</u> &gt;&gt;</span></div>
    <div class="news-item">Harbor Quill is proud to announce that it is the Gold Sponsor of the Northgate CIO Forum 2010<br>Wednesday, April 7, 2010<span class="read-more"><u>Read More</u> &gt;&gt;</span></div>
  </div>
</aside>

<section class="cards">
  <article class="card"><div class="card-art"><div class="card-screen" role="img" aria-label="Monitor showing a bar chart"></div></div>
    <div class="card-body"><h3 class="card-title"><b>Harbor Quill</b> Last Mile Advantage</h3><p class="card-text">Harbor Quill can help you solve real world business problems with complex event processing. Gain an understanding of how Harbor Quill and event processing can help your business.</p></div><span class="card-more">» Learn More</span></article>
  <article class="card"><div class="card-art"><div class="card-screen" role="img" aria-label="Monitor showing an energy product screen"></div></div>
    <div class="card-body"><h3 class="card-title"><b>Desktop</b> Energy Management</h3><p class="card-text">Harbor Quill can help you solve real world business problems with complex event processing. Gain an understanding of how Harbor Quill and event processing can help your business.</p></div><span class="card-more">» Learn More</span></article>
  <article class="card"><div class="card-art"><div class="card-screen" role="img" aria-label="Monitor showing a world map"></div></div>
    <div class="card-body"><h3 class="card-title"><b>Harbor Quill</b> EPN</h3><p class="card-text">Harbor Quill can help you solve real world business problems with complex event processing. Gain an understanding of how Harbor Quill and event processing can help your business.</p></div><span class="card-more">» Learn More</span></article>
  <article class="card"><div class="card-art"><div class="card-screen" role="img" aria-label="Monitor showing a gauge"></div></div>
    <div class="card-body"><h3 class="card-title"><b>Event Driven</b> App. Platform</h3><p class="card-text">Harbor Quill can help you solve real world business problems with complex event processing. Gain an understanding of how Harbor Quill and event processing can help your business.</p></div><span class="card-more">» Learn More</span></article>
</section>

<footer class="footer">
  <div class="copyright">Copyright 2012, <b>Harbor Quill</b></div>
  <ul class="footer-nav"><li>home</li><li>solutions</li><li>technology</li><li>resources</li><li>partners</li><li>company</li><li>support</li></ul>
</footer>
</body>
</html>
```